Nightclub promoter business cards

We need business cards designed for our company based in Toronto, Canada called "NowQuillo". We are an events company that promotes weekly parties in the city. We cater to a 25+ crowd and feel like our brand should reflect that. We are looking for business cards that are textured and contain a unique design. We would prefer black cards. The final design should communicate the finest hospitality and prestige. I've attached files containing our logo. For more info. about our brand visit our website at www.nowquillo-example.com.

Industry/Entity Type

Business

```html
<!DOCTYPE html>
<html lang="en">
<head>
<meta charset="utf-8">
<title>NowQuillo Business Cards</title>
<link rel="stylesheet" href="https://fonts.googleapis.com/css2?family=Questrial&display=swap">
<style>
  :root {
    --backdrop: #d9d8d9;
    --card-edge: #0b0a0a;
    --card-glow: #8d8887;
    --card-mid: #3a3636;
    --accent-blue: #19a6e0;
    --text-light: #f2f2f2;
    --logo-ink: #1d1c1c;
    --rule: rgba(255, 255, 255, 0.12);
  }
  * { margin: 0; padding: 0; box-sizing: border-box; }
  html, body {
    width: 1200px;
    height: 750px;
    overflow: hidden;
    background: var(--backdrop);
    font-family: "Questrial", "Century Gothic", sans-serif;
  }
  .canvas {
    position: relative;
    width: 1200px;
    height: 750px;
    display: flex;
    align-items: center;
    justify-content: center;
    gap: 60px;
  }
  .card {
    position: relative;
    width: 500px;
    height: 286px;
    border-radius: 16px;
    overflow: hidden;
    background: radial-gradient(ellipse 60% 65% at 50% 48%, var(--card-glow) 0%, var(--card-mid) 45%, var(--card-edge) 100%);
    box-shadow: 0 10px 24px rgba(0, 0, 0, 0.25);
  }
  /* contact side */
  .card--contact .pattern-area {
    position: absolute;
    inset: 0;
    width: 100%;
    height: 100%;
  }
  .contact-details {
    position: absolute;
    right: 120px;
    bottom: 62px;
    text-align: right;
    color: var(--text-light);
    font-size: 14px;
    line-height: 1.3;
    letter-spacing: 0.02em;
  }
  /* brand side */
  .card--brand { display: flex; flex-direction: column; align-items: center; justify-content: center; }
  .rule {
    position: absolute;
    left: 24px;
    right: 24px;
    height: 1px;
    background: var(--rule);
  }
  .rule--top { top: 92px; }
  .rule--bottom { top: 200px; }
  .brand-name {
    display: flex;
    align-items: center;
    gap: 12px;
    color: var(--logo-ink);
    font-size: 58px;
    font-weight: 400;
    letter-spacing: -0.02em;
    line-height: 1;
  }
  .brand-dot {
    width: 12px;
    height: 12px;
    border-radius: 50%;
    background: var(--logo-ink);
  }
  .tagline {
    margin-top: 26px;
    color: var(--accent-blue);
    font-size: 19px;
    letter-spacing: 0.02em;
  }
</style>
</head>
<body>
<main class="canvas">

  <section class="card card--contact" aria-label="Card back with contact details">
    <svg class="pattern-area" viewBox="0 0 500 286" role="img" aria-label="Diagonal band of blue, white and black diamond checks">
      <defs>
        <linearGradient id="patternFill" x1="0" y1="1" x2="1" y2="0">
          <stop offset="0" stop-color="#19a6e0" stop-opacity="0.55"/>
          <stop offset="0.35" stop-color="#cfd3d6" stop-opacity="0.55"/>
          <stop offset="0.65" stop-color="#19a6e0" stop-opacity="0.6"/>
          <stop offset="1" stop-color="#e6e6e6" stop-opacity="0.65"/>
        </linearGradient>
        <linearGradient id="patternFade" x1="0" y1="0" x2="0" y2="1">
          <stop offset="0" stop-color="#fff" stop-opacity="1"/>
          <stop offset="1" stop-color="#fff" stop-opacity="0.15"/>
        </linearGradient>
        <mask id="fadeMask"><rect width="500" height="286" fill="url(#patternFade)"/></mask>
      </defs>
      <polygon points="0,150 300,0 500,0 500,70 40,286 0,286" fill="url(#patternFill)" mask="url(#fadeMask)"/>
    </svg>
    <div class="contact-details">
      <p class="contact-phone">+1 647-555-0142</p>
      <p class="contact-web">www.nowquillo-example.com</p>
    </div>
  </section>

  <section class="card card--brand" aria-label="Card front with brand name">
    <span class="rule rule--top"></span>
    <span class="rule rule--bottom"></span>
    <h1 class="brand-name">nowquillo<span class="brand-dot"></span></h1>
    <p class="tagline">It's NowQuillo, you'll know.</p>
  </section>

</main>
</body>
</html>
```